Packaging box for giving wine gifts to customers

I need a nice sturdy elegant box to hold one or two bottles of wine that will give to customers as gifts

Designs look the same

```html
<!DOCTYPE html>
<html lang="en">
<head>
<meta charset="utf-8">
<title>Nortrace Wine Gift Box – Front Panel</title>
<link rel="stylesheet" href="https://fonts.googleapis.com/css2?family=Michroma&display=swap">
<style>
  :root {
    --teal-bright: #23d3c8;
    --teal-mid: #13948f;
    --teal-deep: #0a4f4d;
    --shadow-teal: #0c2d2d;
    --ink: #020707;
    --label: #e9fbfa;
  }
  html, body {
    margin: 0;
    padding: 0;
    width: 774px;
    height: 1200px;
    overflow: hidden;
    background: var(--ink);
  }
  .box-front {
    position: relative;
    width: 774px;
    height: 1200px;
    overflow: hidden;
    background: linear-gradient(160deg, var(--teal-bright) 0%, var(--teal-mid) 45%, var(--teal-deep) 100%);
  }
  .circuit-pattern {
    position: absolute;
    left: 0;
    top: 0;
    width: 774px;
    height: 600px;
    background:
      radial-gradient(ellipse at 60% 20%, rgba(200, 255, 250, 0.28), transparent 60%),
      linear-gradient(180deg, rgba(0, 40, 40, 0.35), rgba(0, 40, 40, 0) 70%);
  }
  .sweep-shapes {
    position: absolute;
    left: 0;
    top: 0;
    width: 774px;
    height: 1200px;
  }
  .brand {
    position: absolute;
    left: 120px;
    bottom: 110px;
    width: 480px;
    color: var(--label);
    font-family: "Michroma", sans-serif;
  }
  .brand-name {
    margin: 0;
    font-size: 48px;
    font-weight: 400;
    letter-spacing: 4px;
    line-height: 1;
    white-space: nowrap;
  }
  .brand-tagline {
    margin: 16px 0 0;
    font-size: 14px;
    letter-spacing: 1.5px;
    white-space: nowrap;
  }
</style>
</head>
<body>
  <main class="box-front">
    <div class="circuit-pattern" role="img" aria-label="Glowing circuit board traces with square and round pads spreading across the top of the box"></div>

    <svg class="sweep-shapes" viewBox="0 0 774 1200" aria-hidden="true">
      <defs>
        <linearGradient id="left-sweep-fill" x1="0" y1="0" x2="0.6" y2="1">
          <stop offset="0" stop-color="var(--shadow-teal)"/>
          <stop offset="0.5" stop-color="#041313"/>
          <stop offset="1" stop-color="var(--ink)"/>
        </linearGradient>
        <linearGradient id="right-sweep-fill" x1="1" y1="0" x2="0" y2="1">
          <stop offset="0" stop-color="#0f3a3a"/>
          <stop offset="0.6" stop-color="#031010"/>
          <stop offset="1" stop-color="var(--ink)"/>
        </linearGradient>
      </defs>
      <path class="right-sweep" d="M774 400 C700 520 660 760 650 1000 L774 1200 Z" fill="url(#right-sweep-fill)"/>
      <path class="left-sweep" d="M0 650 C200 620 380 580 470 540 C520 760 640 1000 774 1200 L0 1200 Z" fill="url(#left-sweep-fill)"/>
    </svg>

    <div class="brand">
      <h1 class="brand-name">Nortrace</h1>
      <p class="brand-tagline">Precision Boards Made With Care</p>
    </div>
  </main>
</body>
</html>
```